Brindle Works - Fast, Efficient and Gas Mainteance for Domestic, Commercial and Industrial clients

We are in the process of purchasing a new business and would like to get a new logo and business card.
Business is a gas maintenance business that also does new gas installations.
Has been established since 1988.
Services include:
Install all types of gas appliances & equipment inc. hot water units
Maintain / repair / replace all types of gas appliances & equipment

Target Market(s)

Domestic, Commercial and Industrial clients

Industry/Entity Type

Business

Contact Information for Business Card

admin@brindleworks-example.com.au
07 5981 4726
Brindle Works PTY LTD

Logo Text

Gas Fitting & Plumbing Maintenance Specialists

Font styles to use
Sans Serif

Requirements
Must have
• Logo
• Business name, contact number, email address, web address
• Domestic | Commercial | Industrial Est Since 1988
Nice to have
• Possibly a black card with a flame logo to one side
Should not have
• Spelling errors

```html
<!DOCTYPE html>
<html lang="en">
<head>
<meta charset="utf-8">
<title>Brindle Works – Business Card</title>
<link href="https://fonts.googleapis.com/css2?family=Montserrat:wght@400;500;800&display=swap" rel="stylesheet">
<style>
  :root {
    --backdrop: #e9e7e4;
    --card-white: #ffffff;
    --card-black: #030303;
    --ink: #111111;
    --ink-soft: #1d1d1d;
    --accent: #f2661f;
    --accent-red: #e83a22;
    --accent-amber: #f7a21b;
    --on-dark: #ffffff;
  }
  * { margin: 0; padding: 0; box-sizing: border-box; }
  html, body {
    width: 1200px; height: 1000px; overflow: hidden;
    background: var(--backdrop);
    font-family: "Montserrat", Arial, sans-serif;
  }
  .canvas { position: relative; width: 1200px; height: 1000px; }

  .card {
    position: absolute; left: 265px; width: 665px; height: 397px;
    border-radius: 22px; overflow: hidden;
    box-shadow: 0 6px 18px rgba(0,0,0,0.25);
  }
  .card--front { top: 73px; background: var(--card-white); }
  .card--back { top: 533px; background: var(--card-black); }

  .brand { position: absolute; display: flex; align-items: center; }
  .brand__dot { border-radius: 50%; background: var(--accent); flex: none; }
  .brand__name {
    font-weight: 800; text-transform: uppercase; letter-spacing: 0.04em;
    line-height: 1.05;
  }
  .card--front .brand { left: 40px; top: 62px; }
  .card--front .brand__dot { width: 78px; height: 78px; margin-right: 40px; }
  .card--front .brand__name { color: var(--ink); font-size: 31px; }

  .card--back .brand { left: 128px; top: 125px; }
  .card--back .brand__dot { width: 110px; height: 110px; margin-right: 55px; }
  .card--back .brand__name { color: var(--on-dark); font-size: 41px; }

  .holder {
    position: absolute; left: 158px; top: 186px;
    color: var(--accent); font-size: 17px; font-weight: 500;
  }
  .contacts { position: absolute; left: 158px; top: 221px; list-style: none; }
  .contacts li {
    display: flex; align-items: center; height: 22px;
    font-size: 15px; color: var(--ink-soft);
  }
  .contacts svg { width: 13px; height: 13px; margin-right: 9px; fill: var(--accent); }
  .services {
    position: absolute; left: 158px; top: 276px; width: 300px;
    font-size: 15px; line-height: 20.5px; color: var(--ink-soft);
  }
  .accent-band {
    position: absolute; left: 0; bottom: 0; width: 100%; height: 18px;
    background: linear-gradient(90deg, var(--accent-red), var(--accent-amber) 50%, var(--accent-red));
  }
</style>
</head>
<body>
<main class="canvas">
  <section class="card card--front" aria-label="Business card front">
    <div class="brand">
      <span class="brand__dot"></span>
      <span class="brand__name">Brindle Works<br>PTY LTD</span>
    </div>
    <p class="holder">Dale Hartley</p>
    <ul class="contacts">
      <li>
        <svg viewBox="0 0 24 24" aria-hidden="true"><path d="M6.6 10.8a15.1 15.1 0 0 0 6.6 6.6l2.2-2.2c.3-.3.7-.4 1-.2 1.1.4 2.3.6 3.6.6.6 0 1 .4 1 1V20c0 .6-.4 1-1 1A17 17 0 0 1 3 4c0-.6.4-1 1-1h3.5c.6 0 1 .4 1 1 0 1.3.2 2.5.6 3.6.1.3 0 .7-.2 1z"/></svg>
        07 5981 4726
      </li>
      <li>
        <svg viewBox="0 0 24 24" aria-hidden="true"><path d="M2 5h20v14H2z M2 5l10 8 10-8" /></svg>
        admin@brindleworks-example.com.au
      </li>
    </ul>
    <p class="services">Install all types of gas appliances &amp; equipment inc. hot water units Maintain / repair / replace all types of gas appliances &amp; equipment</p>
    <div class="accent-band"></div>
  </section>

  <section class="card card--back" aria-label="Business card back">
    <div class="brand">
      <span class="brand__dot"></span>
      <span class="brand__name">Brindle Works<br>PTY LTD</span>
    </div>
  </section>
</main>
</body>
</html>
```